Antigen Preservation Bureau

The company will provide a contract research services to stabilize various viruses, viral vectors, and vaccines. It may offer some licensing opportunities for stabilizing technologies. Main area of applications are pharmaceutical, therapeutic, and vaccination field. The company aspires to develop room temperature vaccines for global distribution beyond the current cold chain.

Target Market(s)

pharmaceutical, therapeutic and vaccination fields

Coding

Coded - Design and coding required

Number of Pages Required

4 page

Requirements
Must have
• Incorporate a APB logo, attached at the bottom, on the Web page

```html
<!DOCTYPE html>
<html lang="en">
<head>
<meta charset="utf-8">
<title>Antigen Preservation Bureau</title>
<link href="https://fonts.googleapis.com/css2?family=Lato:wght@300;400;700;900&display=swap" rel="stylesheet">
<style>
:root{
  --teal:#5e9c84;
  --teal-dark:#3f7a66;
  --mint:#eaf3ef;
  --gold:#c9a44e;
  --ink:#2b2b2b;
  --muted:#6d6d6d;
  --line:#c9c9c9;
  --black:#0e0e0e;
  --white:#ffffff;
  --pin:#d8393a;
}
*{margin:0;padding:0;box-sizing:border-box}
html,body{width:1200px;height:4380px;overflow:hidden}
body{font-family:'Lato',sans-serif;color:var(--ink);background:var(--white);position:relative}
.abs{position:absolute}
.section{position:absolute;left:0;width:1200px;overflow:hidden}
.btn{position:absolute;display:flex;align-items:center;justify-content:center;height:36px;width:120px;border-radius:18px;background:var(--teal);color:var(--white);font-size:13px;font-weight:700}
.divider{position:absolute;width:60px;height:14px}
.h2{position:absolute;font-size:30px;font-weight:400;color:var(--ink)}
.body-text{position:absolute;font-size:13px;line-height:21px;color:var(--muted)}
.lead{position:absolute;font-size:14px;font-weight:700;color:var(--ink)}

/* header & hero */
.hero{top:0;height:678px;background:
  radial-gradient(ellipse 420px 360px at 78% 40%,rgba(236,242,238,.55),transparent 70%),
  radial-gradient(ellipse 300px 260px at 25% 30%,rgba(168,196,150,.6),transparent 70%),
  linear-gradient(100deg,#8fae8a 0%,#6f9a83 35%,#4f8a7c 60%,#9cbcaa 100%)}
.hero-shade{position:absolute;inset:0;background:rgba(60,110,95,.3)}
.brand{position:absolute;left:152px;top:28px;display:flex;align-items:center;gap:10px;color:var(--white)}
.brand-mark{width:26px;height:26px;border:2px solid var(--white)}
.brand-name{font-size:13px;font-weight:700;letter-spacing:1.5px;line-height:15px;width:150px}
.nav{position:absolute;left:563px;top:42px;display:flex;gap:26px;font-size:13px;font-weight:700;color:var(--white);letter-spacing:.5px}
.hero-kicker{position:absolute;top:228px;width:1200px;text-align:center;color:var(--white);font-size:26px;letter-spacing:5px;font-weight:400}
.hero-title{position:absolute;top:266px;width:1200px;text-align:center;color:var(--white);font-size:58px;font-weight:700}
.hero-sub{position:absolute;top:345px;width:1200px;text-align:center;color:#b9e3d3;font-size:12px;letter-spacing:3px;font-weight:700}
.hero-btn{position:absolute;left:482px;top:412px;width:230px;height:38px;border:2px solid var(--white);border-radius:19px;color:var(--white);font-size:13px;letter-spacing:2px;display:flex;align-items:center;justify-content:center;font-weight:700}
.dots{position:absolute;top:602px;left:582px;display:flex;gap:9px}
.dots span{width:9px;height:9px;border-radius:50%;border:1.5px solid var(--white)}
.dots span.on{background:var(--white)}

/* team */
.team{top:678px;height:408px;background:var(--mint)}
.team-photo{position:absolute;left:0;top:0;width:700px;height:408px;background:
  radial-gradient(ellipse 120px 220px at 9% 72%,#fbfcfc,transparent 75%),
  radial-gradient(ellipse 110px 230px at 30% 70%,#f8fafa,transparent 75%),
  radial-gradient(ellipse 110px 220px at 48% 74%,#f6f8f9,transparent 75%),
  radial-gradient(ellipse 120px 230px at 62% 72%,#f4f7f7,transparent 75%),
  radial-gradient(ellipse 90px 60px at 10% 22%,#e4c8b4,transparent 80%),
  radial-gradient(ellipse 90px 60px at 31% 20%,#e1c3ad,transparent 80%),
  radial-gradient(ellipse 80px 60px at 50% 30%,#d9b59d,transparent 80%),
  radial-gradient(ellipse 80px 60px at 62% 24%,#e0c2ac,transparent 80%),
  linear-gradient(180deg,#dfe6e8 0%,#e9eef0 60%,#f1f4f5 100%)}
.team-fade{position:absolute;left:520px;top:0;width:200px;height:408px;background:linear-gradient(90deg,rgba(234,243,239,0),var(--mint))}

/* about */
.about{top:1086px;height:462px;background:var(--white)}

/* research */
.research{top:1548px;height:414px;background:var(--mint)}
.research-photo{position:absolute;left:510px;top:0;width:690px;height:414px;background:
  radial-gradient(ellipse 160px 130px at 22% 52%,rgba(244,176,66,.9),transparent 75%),
  radial-gradient(ellipse 150px 120px at 38% 74%,rgba(238,86,112,.85),transparent 75%),
  radial-gradient(ellipse 140px 170px at 58% 62%,rgba(206,74,170,.8),transparent 75%),
  radial-gradient(ellipse 150px 190px at 76% 48%,rgba(94,118,224,.85),transparent 75%),
  radial-gradient(ellipse 140px 200px at 94% 40%,rgba(46,180,227,.9),transparent 75%),
  radial-gradient(ellipse 260px 120px at 70% 8%,rgba(255,255,255,.9),transparent 75%),
  linear-gradient(90deg,var(--mint) 0%,#f7f3e2 22%,#fbe6c7 50%,#ece0f2 75%,#d9ecf6 100%)}

/* contact */
.contact{top:1962px;height:561px;background:var(--white)}
.field-label{position:absolute;font-size:13px;color:var(--muted)}
.field-label b{color:#d04545;font-weight:700}
.field{position:absolute;width:397px;height:37px;border:1px solid var(--line);background:var(--white)}
.area{position:absolute;left:642px;top:193px;width:316px;height:131px;border:1px solid var(--line)}
.check{position:absolute;left:644px;top:376px;width:14px;height:14px;border:1px solid var(--line)}

/* join */
.join{top:2523px;height:412px;background:
  radial-gradient(ellipse 380px 200px at 45% 60%,rgba(196,160,130,.45),transparent 75%),
  radial-gradient(ellipse 300px 220px at 85% 30%,rgba(170,190,160,.5),transparent 75%),
  linear-gradient(110deg,#3b6d66 0%,#5d8e80 40%,#86a99a 70%,#4c7c72 100%)}
.join-shade{position:absolute;inset:0;background:rgba(40,80,72,.35)}
.join .h2,.join .body-text{color:var(--white)}
.btn-white{background:var(--white);color:var(--ink)}

/* blog */
.blog{top:2935px;height:578px;background:var(--white)}
.card{position:absolute;top:169px;width:272px}
.card-img{height:184px}
.card-title{margin-top:32px;font-size:14px;font-weight:900;letter-spacing:1.2px}
.card-meta{margin-top:8px;font-size:11px;color:var(--muted)}
.card-meta b{color:var(--ink)}
.card-text{margin-top:9px;font-size:11px;line-height:17px;color:var(--muted)}
.card-link{margin-top:20px;font-size:11px;font-weight:900;letter-spacing:1px;color:var(--teal)}

/* map */
.map{top:3513px;height:391px;background:
  radial-gradient(ellipse 260px 140px at 18% 78%,rgba(196,214,170,.9),transparent 75%),
  radial-gradient(ellipse 220px 160px at 82% 22%,rgba(200,220,176,.85),transparent 75%),
  radial-gradient(ellipse 180px 120px at 60% 80%,rgba(214,226,190,.8),transparent 75%),
  radial-gradient(ellipse 200px 110px at 40% 20%,rgba(236,230,210,.9),transparent 75%),
  radial-gradient(ellipse 160px 80px at 96% 90%,rgba(190,214,228,.8),transparent 75%),
  linear-gradient(160deg,#eceee2 0%,#e4e9de 50%,#ece7d8 100%)}
.map-pin{position:absolute;left:540px;top:262px}

/* newsletter */
.newsletter{top:3904px;height:73px;background:var(--teal)}
.news-icon{position:absolute;left:162px;top:17px;width:38px;height:38px;border-radius:50%;background:var(--white)}
.news-title{position:absolute;left:219px;top:22px;font-size:26px;color:var(--white);font-weight:400}
.news-input{position:absolute;left:502px;top:20px;width:394px;height:32px;background:var(--white);font-size:12px;color:var(--muted);padding:9px 12px}
.news-btn{position:absolute;left:911px;top:20px;width:129px;height:32px;background:var(--gold);color:var(--white);font-size:13px;font-weight:700;display:flex;align-items:center;justify-content:center;letter-spacing:1px}

/* footer */
.footer{top:3977px;height:339px;background:var(--black);color:var(--white)}
.foot-h{position:absolute;top:88px;font-size:17px;font-weight:700;letter-spacing:.5px}
.foot-list{position:absolute;font-size:13px;line-height:21px;color:#e3e3e3}
.foot-input{position:absolute;height:37px;background:var(--white);color:var(--ink);font-size:13px;padding:10px 12px}
.foot-send{position:absolute;left:823px;top:216px;width:126px;height:34px;background:var(--gold);display:flex;align-items:center;justify-content:center;font-size:14px;font-weight:700;letter-spacing:1px}
.copyright{top:4316px;height:64px;background:#1c1c1c;color:#9a9a9a;font-size:11px;display:flex;align-items:center;justify-content:center}
</style>
</head>
<body>

<section class="section hero">
  <div class="abs" style="inset:0" role="img" aria-label="Photo of a scientist in a lab coat and gloves holding a sample vial"></div>
  <div class="hero-shade"></div>
  <div class="brand"><span class="brand-mark"></span><span class="brand-name">ANTIGEN PRESERVATION BUREAU</span></div>
  <nav class="nav"><span>HOME</span><span>ABOUT ▾</span><span>TEAM ▾</span><span>RESEARCH ▾</span><span>CONTACT ▾</span><span>JOIN TEAM ▾</span></nav>
  <div class="hero-kicker">DEVELOPING &nbsp;ROOM TEMPERATURE</div>
  <h1 class="hero-title">vaccines for global distribution</h1>
  <div class="hero-sub">BEYOND THE CURRENT COLD CHAIN</div>
  <div class="hero-btn">GET MORE INFORMATION</div>
  <div class="dots"><span class="on"></span><span></span><span></span></div>
</section>

<section class="section team">
  <div class="team-photo" role="img" aria-label="Photo of a research team in white lab coats"></div>
  <div class="team-fade"></div>
  <svg class="divider" style="left:675px;top:62px" viewBox="0 0 60 14"><line x1="0" y1="7" x2="22" y2="7" stroke="#9a9a9a"/><circle cx="30" cy="7" r="4" fill="none" stroke="#9a9a9a"/><line x1="38" y1="7" x2="60" y2="7" stroke="#9a9a9a"/></svg>
  <h2 class="h2" style="left:675px;top:78px">Our Team</h2>
  <div class="lead" style="left:675px;top:142px">Lorem ipsum dolor sit amet, consectetur</div>
  <p class="body-text" style="left:675px;top:178px;width:400px">Lorem ipsum dolor sit amet, consectetur adipiscing elit. Quid autem habent admirationis, cum prope accesseris? An hoc usque quaque, aliter in vita? Non igitur de improbo, sed de callido improbo quaerimus, qualis Q. Nam quibus rebus efficiuntur voluptates.</p>
  <div class="btn" style="left:675px;top:314px">More Info</div>
</section>

<section class="section about">
  <svg class="divider" style="left:570px;top:70px" viewBox="0 0 60 14"><line x1="0" y1="7" x2="22" y2="7" stroke="#9a9a9a"/><circle cx="30" cy="7" r="4" fill="none" stroke="#9a9a9a"/><line x1="38" y1="7" x2="60" y2="7" stroke="#9a9a9a"/></svg>
  <h2 class="h2" style="left:0;width:1200px;text-align:center;top:98px">About Antigen Preservation Bureau</h2>
  <p class="body-text" style="left:155px;width:890px;top:168px;text-align:center">Lorem ipsum dolor sit amet, consectetur adipiscing elit. Quid autem habent admirationis, cum prope accesseris? An hoc usque quaque, aliter in vita? Non igitur de improbo, sed de callido improbo quaerimus, qualis Q. Nam quibus rebus efficiuntur voluptates, eae non sunt in potestate sapientis. Negare non possum. Huic mori optimum esse propter desperationem sapientiae, illi propter spem vivere. Quid enim me prohiberet Epicureum esse, si probarem, quae ille diceret? Quis vero fulvene, quaerere militimus dictur sculis se privasse.</p>
  <p class="body-text" style="left:230px;width:740px;top:282px;text-align:center">Varietates autem iniurasque fortunae facile veteres philosophorum praecepta instituta vita superabat. Et quod est munus, quod opus sapientiae? Non modo carum sibi quemque, verum etiam vehementer carum esse?</p>
  <div class="btn" style="left:540px;top:356px">More Info</div>
</section>

<section class="section research">
  <div class="research-photo" role="img" aria-label="Illustration of colourful test tubes and a molecular model"></div>
  <svg class="divider" style="left:137px;top:60px" viewBox="0 0 60 14"><line x1="0" y1="7" x2="22" y2="7" stroke="#9a9a9a"/><circle cx="30" cy="7" r="4" fill="none" stroke="#9a9a9a"/><line x1="38" y1="7" x2="60" y2="7" stroke="#9a9a9a"/></svg>
  <h2 class="h2" style="left:137px;top:78px">Research</h2>
  <div class="lead" style="left:137px;top:142px">Lorem ipsum dolor sit amet, consectetur</div>
  <p class="body-text" style="left:137px;top:178px;width:390px">Lorem ipsum dolor sit amet, consectetur adipiscing elit. Quid autem habent admirationis, cum prope accesseris? An hoc usque quaque, aliter in vita? Non igitur de improbo, sed de callido improbo quaerimus, qualis Q. Nam quibus rebus efficiuntur voluptates.</p>
  <div class="btn" style="left:137px;top:317px">More Info</div>
</section>

<section class="section contact">
  <svg class="divider" style="left:570px;top:70px" viewBox="0 0 60 14"><line x1="0" y1="7" x2="22" y2="7" stroke="#9a9a9a"/><circle cx="30" cy="7" r="4" fill="none" stroke="#9a9a9a"/><line x1="38" y1="7" x2="60" y2="7" stroke="#9a9a9a"/></svg>
  <h2 class="h2" style="left:0;width:1200px;text-align:center;top:90px">Contact Us</h2>
  <div class="field-label" style="left:166px;top:168px">Name <b>*</b></div>
  <div class="field" style="left:166px;top:191px"></div>
  <div class="field-label" style="left:166px;top:253px">Email <b>*</b></div>
  <div class="field" style="left:166px;top:276px"></div>
  <div class="field-label" style="left:166px;top:338px">Phone</div>
  <div class="field" style="left:166px;top:361px"></div>
  <div class="field-label" style="left:642px;top:168px">Description</div>
  <div class="area"></div>
  <div class="check"></div>
  <div class="field-label" style="left:668px;top:375px;font-size:12px">I have read the Disclaimer and Privacy Policy</div>
  <div class="btn" style="left:540px;top:452px">More Info</div>
</section>

<section class="section join">
  <div class="abs" style="inset:0" role="img" aria-label="Photo of clasped hands in a teamwork gesture"></div>
  <div class="join-shade"></div>
  <svg class="divider" style="left:570px;top:52px" viewBox="0 0 60 14"><line x1="0" y1="7" x2="22" y2="7" stroke="#fff"/><circle cx="30" cy="7" r="4" fill="none" stroke="#fff"/><line x1="38" y1="7" x2="60" y2="7" stroke="#fff"/></svg>
  <h2 class="h2" style="left:0;width:1200px;text-align:center;top:76px">Join Team</h2>
  <p class="body-text" style="left:155px;width:890px;top:142px;text-align:center">Lorem ipsum dolor sit amet, consectetur adipiscing elit. Quid autem habent admirationis, cum prope accesseris? An hoc usque quaque, aliter in vita? Non igitur de improbo, sed de callido improbo quaerimus, qualis Q. Nam quibus rebus efficiuntur voluptates, eae non sunt in potestate sapientis. Negare non possum. Huic mori optimum esse propter desperationem sapientiae, illi propter spem vivere.</p>
  <p class="body-text" style="left:155px;width:890px;top:226px;text-align:center">Varietates autem iniurasque fortunae facile veteres philosophorum praecepta instituta vita superabat. Et quod est munus, quod opus sapientiae? Non modo carum sibi quemque, verum etiam vehementer carum esse? Tu vero isto lecto, sic. Nescium mors esse nosse. Colludu igitur ista te nihil iuvat. Videamus animi partes, quarum est conspectus illustrior.</p>
  <div class="btn btn-white" style="left:540px;top:335px">More Info</div>
</section>

<section class="section blog">
  <svg class="divider" style="left:570px;top:78px" viewBox="0 0 60 14"><line x1="0" y1="7" x2="22" y2="7" stroke="#9a9a9a"/><circle cx="30" cy="7" r="4" fill="none" stroke="#9a9a9a"/><line x1="38" y1="7" x2="60" y2="7" stroke="#9a9a9a"/></svg>
  <h2 class="h2" style="left:0;width:1200px;text-align:center;top:100px">Our Latest Blog Post</h2>
  <article class="card" style="left:160px">
    <div class="card-img" style="background:linear-gradient(135deg,#3c4a5c,#8aa0b4 55%,#d7dde3)" role="img" aria-label="Photo of a laboratory microscope"></div>
    <div class="card-title">LOREM IPSUM DOLOR SIT AMET</div>
    <div class="card-meta">Nov 27, 2016 | <b>ADMIN</b> | Uncategorized</div>
    <div class="card-text">Lorem ipsum dolor sit amet, consectetur adipiscing elit. Quid autem habent admirationis.</div>
    <div class="card-link">CONTINUE &nbsp;→</div>
  </article>
  <article class="card" style="left:461px">
    <div class="card-img" style="background:linear-gradient(135deg,#c9d6e2,#eef2f5 50%,#9fb2c6)" role="img" aria-label="Photo of medical staff in a meeting"></div>
    <div class="card-title">LOREM IPSUM DOLOR SIT AMET</div>
    <div class="card-meta">Dec 02, 2016 | <b>ADMIN</b> | Uncategorized</div>
    <div class="card-text">Lorem ipsum dolor sit amet, consectetur adipiscing elit. Quid autem habent admirationis.</div>
    <div class="card-link">CONTINUE &nbsp;→</div>
  </article>
  <article class="card" style="left:762px">
    <div class="card-img" style="background:linear-gradient(135deg,#5a3a2c,#b7795a 50%,#e9c6a8)" role="img" aria-label="Photo of a researcher examining a sample"></div>
    <div class="card-title">LOREM IPSUM DOLOR SIT AMET</div>
    <div class="card-meta">Jan 05, 2017 | <b>ADMIN</b> | Uncategorized</div>
    <div class="card-text">Lorem ipsum dolor sit amet, consectetur adipiscing elit. Quid autem habent admirationis.</div>
    <div class="card-link">CONTINUE &nbsp;→</div>
  </article>
</section>

<section class="section map">
  <div class="abs" style="inset:0" role="img" aria-label="Road map of the surrounding region around the office"></div>
  <svg class="map-pin" width="26" height="38" viewBox="0 0 26 38" aria-label="Office location marker"><path d="M13 0a13 13 0 0 1 13 13c0 10-13 25-13 25S0 23 0 13A13 13 0 0 1 13 0z" fill="var(--pin)"/><circle cx="13" cy="13" r="4.5" fill="#8e1f20"/></svg>
</section>

<section class="section newsletter">
  <div class="news-icon"></div>
  <svg class="abs" style="left:171px;top:29px" width="20" height="14" viewBox="0 0 20 14"><rect x="1" y="1" width="18" height="12" fill="none" stroke="#5e9c84" stroke-width="2"/><polyline points="1,1 10,8 19,1" fill="none" stroke="#5e9c84" stroke-width="2"/></svg>
  <div class="news-title">News letter Signup</div>
  <div class="news-input">Enter Your Email</div>
  <div class="news-btn">SUBSCRIBE</div>
</section>

<footer class="section footer">
  <div class="brand" style="left:88px;top:86px"><span class="brand-mark"></span><span class="brand-name">ANTIGEN PRESERVATION BUREAU</span></div>
  <p class="foot-list" style="left:88px;top:160px;width:200px;font-size:12px;line-height:18px;color:#bdbdbd">Lorem ipsum dolor sit amet, con sectetur adipiscing elit. Morbi auctor ullamcorper congue. Pha sellus quis lacus quis ante ornare tincidunt lobortis quisquam.</p>

  <div class="foot-h" style="left:342px">CONTACT US</div>
  <svg class="abs" style="left:342px;top:143px" width="12" height="16" viewBox="0 0 12 16"><path d="M6 0a6 6 0 0 1 6 6c0 4-6 10-6 10S0 10 0 6a6 6 0 0 1 6-6z" fill="#fff"/><circle cx="6" cy="6" r="2.2" fill="#0e0e0e"/></svg>
  <div class="foot-list" style="left:372px;top:140px">418 Harwell Ave<br>Fairmont TX 75310</div>
  <svg class="abs" style="left:342px;top:199px" width="13" height="13" viewBox="0 0 13 13"><path d="M2 0l3 3-1.5 2a8 8 0 0 0 4.5 4.5L10 8l3 3-2 2C5 13 0 8 0 2z" fill="#fff"/></svg>
  <div class="foot-list" style="left:372px;top:195px">555.0142.7781</div>
  <svg class="abs" style="left:342px;top:229px" width="14" height="10" viewBox="0 0 14 10"><rect width="14" height="10" fill="#fff"/><polyline points="0,0 7,6 14,0" fill="none" stroke="#0e0e0e"/></svg>
  <div class="foot-list" style="left:372px;top:224px">hello@apb.org</div>

  <div class="foot-h" style="left:607px">ABOUT US</div>
  <div class="foot-list" style="left:607px;top:138px">Home<br>About<br>Team<br>Research<br>Contact<br>Join Team</div>

  <div class="foot-h" style="left:818px">GET IN TOUCH</div>
  <div class="foot-input" style="left:823px;top:126px;width:140px">Name</div>
  <div class="foot-input" style="left:972px;top:126px;width:143px">Phone</div>
  <div class="foot-input" style="left:823px;top:172px;width:292px">Email address</div>
  <div class="foot-send">SEND</div>
</footer>

<div class="section copyright">Copyright © 2017 antigenpreservationbureau.com · All Rights Reserved</div>

</body>
</html>
```